Web design required

1-We need a web design for existing company based in New Zealand
2-We build residential house and light commercial
3-We has in-house designer which allow us can provide interior design
4-We modeling project before site construction, which enable both client and construction team to visually analysis whole project,

Target Market(s)

middle class residential house market
Ref: http://www.brambleworthbuilders.co.nz/

Industry/Entity Type

Construction Company

Number of Pages Required

1 page

Font styles to use
Sans Serif
Other font styles liked:
• Such as : Central Gothic or similar which has more design taste

Colors

Designer to choose colors to be used in the design.

Requirements
Must have
• Front sheet, contact information, sample project

```html
<!DOCTYPE html>
<html lang="en">
<head>
<meta charset="utf-8">
<title>Kestrel Homes</title>
<link href="https://fonts.googleapis.com/css2?family=Didact+Gothic&family=Montserrat:wght@500;600;700&display=swap" rel="stylesheet">
<style>
:root{
  --ink:#111;
  --text:#555;
  --muted:#888;
  --rule:#e2e2e2;
  --brand:#1f5f9e;
  --sky:#dbeaf6;
  --sand:#ede6da;
  --bar:#000;
  --white:#fff;
  --social-a:#2f5da8;
  --social-b:#2aa3d9;
  --social-c:#1f74b4;
  --social-d:#f0892a;
}
*{margin:0;padding:0;box-sizing:border-box}
html,body{width:1200px;height:3061px;overflow:hidden;background:var(--white)}
body{position:relative;font-family:"Didact Gothic",sans-serif;color:var(--text)}
.abs{position:absolute}
.topbar{left:0;top:0;width:1200px;height:41px;background:var(--bar)}
.topbar .welcome{left:67px;top:12px;color:var(--white);font-size:14px}
.topbar .search{left:914px;top:6px;width:219px;height:29px;background:var(--white);font-size:11px;color:#999;padding:8px 10px}
.brand{left:0;top:84px;width:1200px;display:flex;justify-content:center;align-items:center;gap:16px}
.brand .mark{width:60px;height:60px;background:var(--brand)}
.brand .name{font-family:"Montserrat",sans-serif;font-weight:600;font-size:34px;letter-spacing:6px;color:var(--ink)}
.nav{top:193px;left:0;width:1200px;height:30px}
.nav a{position:absolute;font-family:"Montserrat",sans-serif;font-weight:500;font-size:12px;color:var(--muted);text-decoration:none;letter-spacing:.5px}
.nav a.current{color:var(--ink);font-weight:700}
.nav .caret{left:380px;top:19px;width:0;height:0;border-left:5px solid transparent;border-right:5px solid transparent;border-bottom:7px solid var(--ink)}
.rule{height:2px;background:var(--rule)}
.photo{display:block}
.hero{left:67px;top:247px;width:1066px;height:541px;background:
  linear-gradient(90deg,rgba(255,255,255,0) 0%,rgba(255,255,255,0) 55%,rgba(40,60,40,.35) 90%,rgba(255,255,255,0) 100%),
  linear-gradient(180deg,#6d8fb5 0%,#b9c9da 16%,#e9eef2 30%,#f2f3f3 40%,#c9ced2 50%,#9aa2a8 55%,#2f4a25 58%,#243d1e 74%,#6f8f3a 78%,#91a94e 100%)}
.hero-title{left:131px;top:398px;font-family:"Montserrat",sans-serif;font-weight:700;font-size:56px;line-height:74px}
.hero-title .line{width:196px;height:3px;background:var(--ink);margin-bottom:6px}
.hero-title .a{color:var(--brand)}
.hero-title .b{color:var(--white)}
.panel h2{font-family:"Montserrat",sans-serif;font-weight:600;font-size:25px;line-height:33px;color:var(--ink)}
.panel p{font-size:16px;line-height:25px;color:var(--muted);margin-top:20px}
.btn{position:absolute;border:2px solid var(--ink);border-radius:6px;font-family:"Montserrat",sans-serif;font-weight:600;font-size:15px;color:var(--ink);display:flex;align-items:center;justify-content:center;width:139px;height:55px}
.build-photo{left:67px;top:808px;width:527px;height:419px;background:
  linear-gradient(180deg,rgba(255,255,255,0) 0%,rgba(255,255,255,0) 52%,rgba(160,104,52,.55) 62%,rgba(240,238,232,.2) 75%,rgba(255,255,255,0) 100%) 295px 0/232px 419px no-repeat,
  linear-gradient(90deg,#b9773c 0%,#d9a16a 20%,#f1ece4 45%,#2a2a2a 55%,#f5f3ef 57%,#f5f3ef 100%)}
.build-panel{left:608px;top:808px;width:525px;height:419px;background:var(--sky);padding:56px 43px}
.build-panel::before{content:"";position:absolute;left:-14px;top:40px;border-top:14px solid transparent;border-bottom:14px solid transparent;border-right:14px solid var(--sky)}
.build-panel .btn{left:43px;top:300px}
.about-panel{left:67px;top:1247px;width:527px;height:437px;background:var(--sand);padding:56px 53px;text-align:right}
.about-panel::after{content:"";position:absolute;right:-14px;top:40px;border-top:14px solid transparent;border-bottom:14px solid transparent;border-left:14px solid var(--sand)}
.about-panel .btn{right:53px;top:300px}
.about-photo{left:608px;top:1247px;width:525px;height:437px;background:
  linear-gradient(90deg,rgba(30,35,45,.55) 0%,rgba(30,35,45,0) 25%,rgba(255,200,110,.35) 60%,rgba(30,35,45,.2) 100%),
  linear-gradient(180deg,#2c58a0 0%,#4f78b8 18%,#eef0f2 35%,#e4e6e8 60%,#8d8f92 72%,#a3a19c 90%,#6b4a32 100%)}
.section-head{left:67px;width:1066px;display:flex;align-items:center;gap:28px}
.section-head::before,.section-head::after{content:"";flex:1;height:1px;background:var(--rule)}
.section-head h3{font-family:"Montserrat",sans-serif;font-weight:700;font-size:19px;color:var(--ink);letter-spacing:.5px}
.card{width:343px;text-align:center}
.card .photo{width:343px;height:338px}
.card .title{font-size:15px;color:var(--ink);margin-top:16px}
.card .link{font-size:11px;color:var(--muted);text-decoration:underline;margin-top:5px}
.service{width:343px;text-align:center}
.service .title{font-size:15px;color:var(--ink)}
.service .more{font-size:13px;color:var(--muted);margin-top:4px}
.service .photo{width:343px;height:337px;margin-top:10px}
.service p{text-align:left;font-size:13px;line-height:20px;color:var(--muted);margin-top:22px}
.footer-col h4{font-family:"Montserrat",sans-serif;font-weight:600;font-size:15px;color:var(--ink);padding-bottom:10px;border-bottom:2px solid var(--rule);width:166px}
.footer-col p{font-size:13px;line-height:21px;color:var(--muted);margin-top:16px}
.contact-row{display:flex;align-items:flex-start;gap:10px;font-size:13px;line-height:19px;color:var(--muted);margin-top:12px}
.contact-row svg{flex:none;margin-top:2px}
.sub-input{position:absolute;left:714px;top:2866px;width:300px;height:38px;border:1px solid var(--rule);font-size:10px;color:var(--muted);padding:13px 12px}
.sub-btn{position:absolute;left:1014px;top:2866px;width:119px;height:38px;background:var(--ink);color:var(--white);font-family:"Montserrat",sans-serif;font-weight:700;font-size:13px;display:flex;align-items:center;justify-content:center}
.copyright{left:67px;top:3019px;font-size:12px;color:var(--muted)}
.copyright b{color:var(--ink);font-weight:400}
.social{left:1004px;top:3015px;display:flex;gap:11px}
.social span{width:24px;height:24px;border-radius:2px}
.social .s1{background:var(--social-a)}
.social .s2{background:var(--social-b)}
.social .s3{background:var(--social-c)}
.social .s4{background:var(--social-d)}
</style>
</head>
<body>
<header>
  <div class="abs topbar">
    <div class="abs welcome">Welcome To The Kestrel Homes</div>
    <div class="abs search">Search</div>
  </div>
  <div class="abs brand"><span class="mark"></span><span class="name">KESTREL HOMES</span></div>
  <nav class="abs nav">
    <a class="current" style="left:369px;top:0">HOME</a>
    <span class="abs caret"></span>
    <a style="left:451px;top:0">SERVICES</a>
    <a style="left:555px;top:0">ABOUT US</a>
    <a style="left:659px;top:0">PROJECTS</a>
    <a style="left:765px;top:0">CONTACT</a>
  </nav>
  <div class="abs rule" style="left:67px;top:222px;width:1066px"></div>
</header>

<main>
  <div class="abs hero photo" role="img" aria-label="White two-storey family home with a grey metal roof behind a green hedge and lawn"></div>
  <div class="abs hero-title"><div class="line"></div><div class="a">KESTREL</div><div class="b">HOMES</div></div>

  <div class="abs build-photo photo" role="img" aria-label="Interior details of floating timber staircase and timber ceiling"></div>
  <section class="abs build-panel panel">
    <h2>WE BUILD RESIDENTIAL HOUSE<br>AND LIGHT COMMERCIAL</h2>
    <p>Kestrel Homes is dedicated to creating and renovating<br>beautiful and unusual buildings.</p>
    <p>Kestrel Homes works with you to take dream houses off<br>the blueprints and into reality.</p>
    <a class="btn">READ MORE</a>
  </section>

  <section class="abs about-panel panel">
    <h2>ABOUT US</h2>
    <p>Kestrel Homes is dedicated to creating and renovating<br>beautiful and unusual buildings.</p>
    <p>Kestrel Homes works with you to take dream houses off<br>the blueprints and into reality. We have the knowl-<br>edge and expertise to customise homes to suit you –</p>
    <a class="btn">READ MORE</a>
  </section>
  <div class="abs about-photo photo" role="img" aria-label="Modern weatherboard home at dusk with warm lit windows and a garage"></div>

  <div class="abs section-head" style="top:1716px"><h3>FEATURED PROJECTS</h3></div>
  <div class="abs card" style="left:67px;top:1772px">
    <div class="photo" role="img" aria-label="House under construction wrapped in scaffolding" style="background:linear-gradient(90deg,rgba(90,95,100,.25) 0%,rgba(255,255,255,0) 50%,rgba(90,95,100,.3) 100%),linear-gradient(180deg,#3f6fb0 0%,#b7c7da 18%,#e8eaec 32%,#c9cdd1 55%,#8e9398 80%,#55683d 100%)"></div>
    <div class="title">Projects - 1</div><div class="link">Click Here</div>
  </div>
  <div class="abs card" style="left:429px;top:1772px">
    <div class="photo" role="img" aria-label="Contemporary dark clad two-storey home with detail views" style="background:linear-gradient(180deg,#eeeeec 0%,#dcdcda 10%,#4a4a4a 20%,#2b2b2b 50%,#5f5a52 62%,#8c8c88 75%,#a08a70 100%)"></div>
    <div class="title">Projects - 2</div><div class="link">Click Here</div>
  </div>
  <div class="abs card" style="left:792px;top:1772px">
    <div class="photo" role="img" aria-label="White bungalow behind a rendered front wall with garden plants" style="background:linear-gradient(180deg,#6e93b8 0%,#2e3d2a 18%,#4c5a49 38%,#f2f2f0 45%,#eeeeec 75%,#6d7a56 85%,#8a8a84 100%)"></div>
    <div class="title">Projects - 3</div><div class="link">Click Here</div>
  </div>

  <div class="abs section-head" style="top:2220px"><h3>OUR SERVICES</h3></div>
  <div class="abs service" style="left:67px;top:2274px">
    <div class="title">Preconstruction Planning</div><div class="more">Read More</div>
    <div class="photo" role="img" aria-label="Hands reviewing building plans on a desk" style="background:linear-gradient(160deg,#5a5f6a 0%,#c9a58c 20%,#e9e9ea 45%,#f4f4f4 70%,#dcdde0 100%)"></div>
    <p>Lorem ipsum dolor sit amet, consectetur adipiscing elit. Pellentesque tempus tellus eget sem viverra, eu elementum dolor bibendum.</p>
  </div>
  <div class="abs service" style="left:429px;top:2278px">
    <div class="title">Construction Modelling</div><div class="more">Read More</div>
    <div class="photo" role="img" aria-label="3D model rendering of a house on a plain background" style="background:radial-gradient(ellipse 45% 22% at 48% 50%,#b9b3a3 0%,#d8d4c8 50%,rgba(250,250,246,0) 100%),#fafaf6;border:1px solid var(--rule)"></div>
    <p>Lorem ipsum dolor sit amet, consectetur adipiscing elit. Pellentesque tempus tellus eget sem viverra, eu elementum dolor bibendum.</p>
  </div>
  <div class="abs service" style="left:792px;top:2278px">
    <div class="title">Full Project Management</div><div class="more">Read More</div>
    <div class="photo" role="img" aria-label="Site team in hard hats reviewing plans on a construction site" style="background:linear-gradient(180deg,#2f3236 0%,#8b857c 30%,#a8754a 50%,#3b4150 68%,#c7c6c0 85%,#b4b2aa 100%)"></div>
    <p>Lorem ipsum dolor sit amet, consectetur adipiscing elit. Pellentesque tempus tellus eget sem viverra, eu elementum dolor bibendum.</p>
  </div>
</main>

<footer>
  <div class="abs rule" style="left:67px;top:2790px;width:1066px;height:1px"></div>
  <div class="abs footer-col" style="left:67px;top:2818px">
    <h4>Employment</h4>
    <p>To apply for a job with Kestrel Homes,<br>please send a cover letter together<br>with ur C.V. to: info@kestrelhomes.co.nz</p>
  </div>
  <div class="abs footer-col" style="left:422px;top:2818px">
    <h4>Head Office</h4>
    <div class="contact-row"><svg width="12" height="16" viewBox="0 0 12 16"><path d="M6 0a6 6 0 0 0-6 6c0 4.5 6 10 6 10s6-5.5 6-10a6 6 0 0 0-6-6zm0 8.5A2.5 2.5 0 1 1 6 3.5a2.5 2.5 0 0 1 0 5z" fill="#888"/></svg><span>18 Harrowfield Lane,<br>Eastmere Auckland</span></div>
    <div class="contact-row"><svg width="13" height="10" viewBox="0 0 13 10"><rect width="13" height="10" fill="#888"/><path d="M0 0l6.5 5L13 0" stroke="#fff" fill="none"/></svg><span>info@kestrelhomes.co.nz</span></div>
    <div class="contact-row"><svg width="12" height="12" viewBox="0 0 12 12"><path d="M2 0l2.5 3-1.3 1.6a7 7 0 0 0 4.2 4.2L9 7.5 12 10l-1.5 2C5 12 0 7 0 1.5z" fill="#888"/></svg><span>Tel: 0064 9 555 0142</span></div>
  </div>
  <div class="abs footer-col" style="left:714px;top:2818px"><h4>Subscribe</h4></div>
  <div class="sub-input">Enter Your Email Address :</div>
  <div class="sub-btn">SUBSCRIBE</div>
  <div class="abs rule" style="left:67px;top:2996px;width:1066px;height:1px"></div>
  <div class="abs copyright">Copyright © 2017 <b>Kestrel Homes</b>. All Rights Reserved.</div>
  <div class="abs social" aria-label="Social links"><span class="s1"></span><span class="s2"></span><span class="s3"></span><span class="s4"></span></div>
</footer>
</body>
</html>
```